Making Hours Count Quorvo App

I am looking to create an Quorvo app (support Quorvo 7 and above) that will inspire and empower the app user to be more productive through a creative, interative and simplistic user experience that teaches the 10 topics related to "Making Hours Count". Please see attached zip files for the 10 topic as PDF files and 20 posters (20 jpg files) which include a quote related to the content bundle’s topic.

Target Market(s)

working professionals who desire to be more productive in their ways of doing

Industry/Entity Type

It Support

Font styles to use
Sans Serif

Colors
33a6d7
0255a3
9bcb3b
cadf82
33b8a4

Requirements
Must have
• don't really wanna say "ebook" style app which would be below my expectation, i expect something more creative than an "ebook" app. i prefer you use your creativity to come up with the design but if you are a bit lost, please read below.
• some specs in my mind:
• - 10 flash cards design for each of the topic so they can be used in a carousel style menu (see sample app screenshot 1 - 1st screen to the left)
• - when presenting a topic, the background should be the same as the flash card of the topic (see sample app screenshot 2 - the right most screen)
• - at the bottom of the topic screen, a audio play/pause buttons bar should be presented as the app will play audible version for the article.
• - the fashion of the sample app screen shots shouldn't be followed as it is an ancient fashion reflecting the content. I expect the fashion of the app should be modern and reflect the topic "making hours count"
• Screens required:
• - Main menu screen: carosoul style presenting the 10 topics using flash cards, should have a "play/pause" button to play the audible topic
• - Topic screen: presents the text content of the topic with flash card design as the background, paging buttons when content spans over one page, have media player bar at bottom to "play/pause/fast forward/reverse" audible
Nice to have
• i have 20 posters with quotes that inspires the user. i would like to see the posters to be presented full screen with a "inspire me" button somewhere which will randomly display a poster to the user.

```html
<!DOCTYPE html>
<html lang="en">
<head>
<meta charset="utf-8">
<title>Making Hours Count – App Screens</title>
<link rel="stylesheet" href="https://fonts.googleapis.com/css2?family=Nunito+Sans:wght@400;600;700&family=Noto+Serif:wght@400;700&display=swap">
<style>
  :root {
    --board: #7a918b;
    --teal: #35b59c;
    --teal-dark: #2a9d87;
    --ink: #1e1e1e;
    --muted: #444;
    --white: #ffffff;
    --line: #d8dcdc;
    --scene-top: #eef2f3;
    --scene-bottom: #dfe7ea;
    --tile-blue: #2f8bc6;
    --tile-yellow: #e0c53b;
    --tile-pink: #d94e9f;
    --tile-purple: #7a3f9f;
    --tile-teal: #3fcdb1;
    --tile-orange: #e8913f;
    --black: #000000;
  }
  * { box-sizing: border-box; margin: 0; padding: 0; }
  html, body { width: 699px; height: 1200px; overflow: hidden; }
  body { background: var(--board); font-family: "Nunito Sans", Arial, sans-serif; color: var(--ink); position: relative; }

  .screen { position: absolute; width: 320px; overflow: hidden; background: linear-gradient(180deg, var(--scene-top), var(--scene-bottom)); }
  .screen--menu-grid { left: 20px; top: 12px; height: 575px; }
  .screen--menu-carousel { left: 359px; top: 12px; height: 575px; }
  .screen--topic { left: 20px; top: 612px; height: 568px; }
  .screen--poster { left: 359px; top: 612px; height: 568px; background: var(--black); }

  .status-bar { position: absolute; left: 0; top: 0; width: 100%; height: 20px; font-size: 12px; display: flex; align-items: center; padding: 0 6px; }
  .status-bar__carrier { display: flex; align-items: center; gap: 3px; }
  .signal-dots { display: flex; gap: 1.5px; }
  .signal-dots span { width: 5px; height: 5px; border-radius: 50%; background: var(--ink); }
  .signal-dots span.off { background: none; border: 1px solid var(--ink); }
  .status-bar__time { position: absolute; left: 0; right: 0; text-align: center; font-weight: 600; }
  .status-bar__battery { margin-left: auto; display: flex; align-items: center; gap: 3px; }
  .battery { width: 22px; height: 10px; border: 1px solid var(--ink); border-radius: 2px; padding: 1px; position: relative; }
  .battery::before { content: ""; display: block; width: 100%; height: 100%; background: var(--ink); }
  .battery::after { content: ""; position: absolute; right: -3px; top: 2px; width: 2px; height: 4px; background: var(--ink); }

  .app-header { position: absolute; left: 0; top: 0; width: 100%; height: 113px; background: var(--white); border-bottom: 1px solid var(--line); }
  .app-header__mark { position: absolute; left: 16px; top: 26px; width: 22px; height: 22px; border-radius: 50%; background: var(--teal); }
  .app-header__title { position: absolute; left: 0; right: 0; top: 38px; text-align: center; font-size: 17px; font-weight: 600; }
  .view-switch { position: absolute; left: 84px; top: 72px; width: 152px; height: 28px; border: 1px solid var(--teal); border-radius: 4px; display: flex; overflow: hidden; }
  .view-switch__option { flex: 1; display: flex; align-items: center; justify-content: center; background: var(--white); }
  .view-switch__option.is-active { background: var(--teal); }

  .topic-grid { position: absolute; left: 0; top: 135px; width: 100%; }
  .topic-tile { position: absolute; width: 100px; text-align: center; }
  .topic-tile__card { width: 68px; height: 84px; margin: 0 auto; border-radius: 4px; color: var(--white); font-size: 30px; display: flex; align-items: center; justify-content: center; box-shadow: 0 1px 3px rgba(0,0,0,.25); }
  .topic-tile__label { font-size: 11.5px; line-height: 14px; margin-top: 3px; color: var(--ink); }
  .card-art--alarm { background: linear-gradient(160deg, #7a1c12, #d8452a 55%, #3a0f0b); }
  .card-art--tree { background: linear-gradient(180deg, #8fc7e4, #e8eef0 60%, #bfcfd6); }
  .card-art--typing { background: linear-gradient(180deg, #e7cfc3, #e8b0a0 55%, #d8c9c2); }

  .audio-bar { position: absolute; left: 0; bottom: 0; width: 100%; height: 44px; background: var(--white); border-top: 1px solid var(--line); display: flex; align-items: center; padding: 0 14px 0 16px; }
  .audio-bar__label { font-size: 17px; margin-left: 10px; }
  .toggle { margin-left: auto; width: 50px; height: 30px; border-radius: 15px; background: var(--teal); position: relative; }
  .toggle::after { content: ""; position: absolute; right: 2px; top: 2px; width: 26px; height: 26px; border-radius: 50%; background: var(--white); box-shadow: 0 1px 3px rgba(0,0,0,.3); }

  .carousel { position: absolute; left: 0; top: 160px; width: 100%; height: 260px; perspective: 500px; }
  .carousel__card { position: absolute; box-shadow: 0 2px 6px rgba(0,0,0,.3); }
  .carousel__card--prev { left: 8px; top: 20px; width: 58px; height: 230px; transform: rotateY(35deg); transform-origin: left center; }
  .carousel__card--current { left: 76px; top: 13px; width: 168px; height: 230px; }
  .carousel__card--next { left: 254px; top: 20px; width: 52px; height: 230px; transform: rotateY(-35deg); transform-origin: right center; opacity: .75; }
  .carousel__title { position: absolute; left: 0; right: 0; top: 408px; text-align: center; font-size: 16.5px; font-weight: 700; line-height: 21px; }
  .carousel__count { position: absolute; left: 0; right: 0; top: 470px; text-align: center; font-size: 15.5px; font-weight: 700; }

  .topic-header { position: absolute; left: 0; top: 32px; width: 100%; }
  .back-link { position: absolute; left: 10px; top: 0; }
  .topic-header__title { font-family: "Noto Serif", Georgia, serif; font-weight: 700; font-size: 15px; line-height: 20px; text-align: center; padding: 0 40px; }
  .topic-body { position: absolute; left: 17px; top: 106px; width: 292px; font-family: "Noto Serif", Georgia, serif; font-size: 15px; line-height: 24.6px; color: #222; }
  .topic-body p { text-indent: 4px; margin-bottom: 24px; }
  .player-bar { position: absolute; left: 0; bottom: 0; width: 100%; height: 44px; background: var(--white); border-top: 1px solid var(--line); display: flex; align-items: center; justify-content: space-between; padding: 0 12px 0 16px; }
  .text-size { color: var(--teal); font-weight: 600; letter-spacing: -.5px; }
  .text-size small { font-size: 10px; }
  .text-size span { font-size: 13px; }
  .text-size b { font-size: 17px; font-weight: 600; }

  .close-button { position: absolute; right: 19px; top: 19px; }
  .poster-art { position: absolute; left: 0; top: 84px; width: 320px; height: 400px; background: linear-gradient(180deg, #2d2f33 0%, #2d2f33 25%, #49c3a9 40%, #f3ecc8 55%, #2d2f33 70%, #e2524a 82%, #e2524a 100%); }
</style>
</head>
<body>

<section class="screen screen--menu-grid">
  <header class="app-header">
    <div class="status-bar">
      <div class="status-bar__carrier"><span class="signal-dots"><span></span><span></span><span></span><span class="off"></span><span class="off"></span></span> Veltra
        <svg width="12" height="9" viewBox="0 0 12 9"><path d="M6 8.5 L1 3 A7 7 0 0 1 11 3 Z" fill="#1e1e1e"/></svg></div>
      <div class="status-bar__time">4:21 PM</div>
      <div class="status-bar__battery">100% <span class="battery"></span></div>
    </div>
    <span class="app-header__mark"></span>
    <h1 class="app-header__title">Making Hours Count</h1>
    <div class="view-switch">
      <span class="view-switch__option is-active">
        <svg width="16" height="16" viewBox="0 0 16 16" fill="#fff"><rect x="0" y="0" width="4" height="4"/><rect x="6" y="0" width="4" height="4"/><rect x="12" y="0" width="4" height="4"/><rect x="0" y="6" width="4" height="4"/><rect x="6" y="6" width="4" height="4"/><rect x="12" y="6" width="4" height="4"/><rect x="0" y="12" width="4" height="4"/><rect x="6" y="12" width="4" height="4"/><rect x="12" y="12" width="4" height="4"/></svg>
      </span>
      <span class="view-switch__option">
        <svg width="18" height="16" viewBox="0 0 18 16" fill="#35b59c"><rect x="0" y="3" width="3" height="10"/><rect x="5" y="0" width="8" height="16"/><rect x="15" y="3" width="3" height="10"/></svg>
      </span>
    </div>
  </header>

  <div class="topic-grid">
    <div class="topic-tile" style="left:10px;top:0"><div class="topic-tile__card" style="background:var(--tile-blue)">01</div><p class="topic-tile__label">An Introduction<br>to Highly Pro...</p></div>
    <div class="topic-tile" style="left:110px;top:0"><div class="topic-tile__card card-art--alarm" role="img" aria-label="Card art: raised hand warning sign over red flames"></div><p class="topic-tile__label">How to Avoid<br>Distractions</p></div>
    <div class="topic-tile" style="left:211px;top:0"><div class="topic-tile__card card-art--tree" role="img" aria-label="Card art: tree with light-bulb leaves in a snowy landscape"></div><p class="topic-tile__label">How to Have<br>the Most Pro...</p></div>
    <div class="topic-tile" style="left:10px;top:129px"><div class="topic-tile__card card-art--typing" role="img" aria-label="Card art: hands over a keyboard"></div><p class="topic-tile__label">How to Speed<br>Up Your Typi...</p></div>
    <div class="topic-tile" style="left:110px;top:129px"><div class="topic-tile__card" style="background:var(--tile-yellow)">05</div><p class="topic-tile__label">How to Spend<br>Less Time on...</p></div>
    <div class="topic-tile" style="left:211px;top:129px"><div class="topic-tile__card" style="background:var(--tile-pink)">06</div><p class="topic-tile__label">Incentivizing<br>Productivity vs...</p></div>
    <div class="topic-tile" style="left:10px;top:263px"><div class="topic-tile__card" style="background:var(--tile-purple)">07</div><p class="topic-tile__label">Productivity is<br>Happiness</p></div>
    <div class="topic-tile" style="left:110px;top:263px"><div class="topic-tile__card" style="background:var(--tile-teal)">08</div><p class="topic-tile__label">Try This One<br>Smart Trick to...</p></div>
    <div class="topic-tile" style="left:211px;top:263px"><div class="topic-tile__card" style="background:var(--tile-orange)">09</div><p class="topic-tile__label">Why Nutrition<br>and Producti...</p></div>
  </div>

  <footer class="audio-bar">
    <svg width="22" height="24" viewBox="0 0 22 24" fill="#555"><path d="M7 3 L21 0 V17 A3.5 3 0 1 1 18.5 14.2 V5 L9.5 7 V20 A3.5 3 0 1 1 7 17.2 Z"/></svg>
    <span class="audio-bar__label">Audio Background</span>
    <span class="toggle"></span>
  </footer>
</section>

<section class="screen screen--menu-carousel">
  <header class="app-header">
    <div class="status-bar">
      <div class="status-bar__carrier"><span class="signal-dots"><span></span><span></span><span></span><span class="off"></span><span class="off"></span></span> Veltra
        <svg width="12" height="9" viewBox="0 0 12 9"><path d="M6 8.5 L1 3 A7 7 0 0 1 11 3 Z" fill="#1e1e1e"/></svg></div>
      <div class="status-bar__time">4:21 PM</div>
      <div class="status-bar__battery">100% <span class="battery"></span></div>
    </div>
    <span class="app-header__mark"></span>
    <h1 class="app-header__title">Making Hours Count</h1>
    <div class="view-switch">
      <span class="view-switch__option">
        <svg width="16" height="16" viewBox="0 0 16 16" fill="#35b59c"><rect x="0" y="0" width="4" height="4"/><rect x="6" y="0" width="4" height="4"/><rect x="12" y="0" width="4" height="4"/><rect x="0" y="6" width="4" height="4"/><rect x="6" y="6" width="4" height="4"/><rect x="12" y="6" width="4" height="4"/><rect x="0" y="12" width="4" height="4"/><rect x="6" y="12" width="4" height="4"/><rect x="12" y="12" width="4" height="4"/></svg>
      </span>
      <span class="view-switch__option is-active">
        <svg width="18" height="16" viewBox="0 0 18 16" fill="#fff"><rect x="0" y="3" width="3" height="10"/><rect x="5" y="0" width="8" height="16"/><rect x="15" y="3" width="3" height="10"/></svg>
      </span>
    </div>
  </header>

  <div class="carousel">
    <div class="carousel__card carousel__card--prev card-art--alarm" role="img" aria-label="Card art: raised hand warning sign over red flames"></div>
    <div class="carousel__card carousel__card--current card-art--tree" role="img" aria-label="Card art: tree with light-bulb leaves in a snowy landscape"></div>
    <div class="carousel__card carousel__card--next card-art--typing" role="img" aria-label="Card art: hands over a keyboard"></div>
  </div>
  <h2 class="carousel__title">How to Have the Most Productive Day<br>Possible Using Hacks</h2>
  <p class="carousel__count">(3 of 10)</p>

  <footer class="audio-bar">
    <svg width="22" height="24" viewBox="0 0 22 24" fill="#555"><path d="M7 3 L21 0 V17 A3.5 3 0 1 1 18.5 14.2 V5 L9.5 7 V20 A3.5 3 0 1 1 7 17.2 Z"/></svg>
    <span class="audio-bar__label">Audio Background</span>
    <span class="toggle"></span>
  </footer>
</section>

<section class="screen screen--topic">
  <div class="status-bar">
    <div class="status-bar__carrier"><span class="signal-dots"><span></span><span></span><span></span><span class="off"></span><span class="off"></span></span> Veltra
      <svg width="12" height="9" viewBox="0 0 12 9"><path d="M6 8.5 L1 3 A7 7 0 0 1 11 3 Z" fill="#1e1e1e"/></svg></div>
    <div class="status-bar__time">4:21 PM</div>
    <div class="status-bar__battery">100% <span class="battery"></span></div>
  </div>
  <header class="topic-header">
    <svg class="back-link" width="14" height="22" viewBox="0 0 14 22"><path d="M11 2 L3 11 L11 20" fill="none" stroke="#35b59c" stroke-width="2.5"/></svg>
    <h2 class="topic-header__title">How to Have the Most Productive Day Possible Using Hacks</h2>
  </header>
  <article class="topic-body">
    <p>If you read the advice of productivity gurus then you will find they often give tips and advice on ways that you can increase your output and productivity through clever lifestyle hacks. These include little changes to your routine and workflow that help to make you more engaged, less distracted and more full of energy.</p>
    <p>On their own, these tips and hacks tend to have only a minor impact. But what if you try them all at once? Then you would get a cumulative effect that should drastically increase your productivity.</p>
  </article>
  <footer class="player-bar">
    <svg width="12" height="18" viewBox="0 0 12 18"><path d="M9 2 L3 9 L9 16" fill="none" stroke="#35b59c" stroke-width="2.2"/></svg>
    <span class="text-size"><small>A</small><span>A</span><b>A</b></span>
    <svg width="18" height="20" viewBox="0 0 18 20" fill="#35b59c"><rect x="1" y="0" width="6" height="20"/><rect x="11" y="0" width="6" height="20"/></svg>
    <span style="width:1px"></span>
    <svg width="12" height="18" viewBox="0 0 12 18"><path d="M3 2 L9 9 L3 16" fill="none" stroke="#35b59c" stroke-width="2.2"/></svg>
  </footer>
</section>

<section class="screen screen--poster">
  <svg class="close-button" width="22" height="22" viewBox="0 0 22 22"><path d="M2 2 L20 20 M20 2 L2 20" stroke="#fff" stroke-width="2.5"/></svg>
  <div class="poster-art" role="img" aria-label="Quote poster in hand lettering: It's not knowing what to do, it's doing what you know. – Dale Morrow"></div>
</section>

</body>
</html>
```